Fresh Label design - High-performance, Enviro-friendly, Versatile, Concentrated cleaning product

I need a 10"L x 5"H label for our cleaning product. (PLEASE DO NOT JUST DO A RE-HASH OF OUR EXISTING LABEL. Come up with something fresh)
Our target markets are Powersports, -Dirtbike/ATV/Boats, RV's, Mountain bikes, Automotive ,Farm/Construction, etc.
Our ideal customers are outdoor oriented people, 18-75, with disposable income. The label needs to work in both a big box store, as well as independent powersports and RV stores, etc.
They need to be cost effective for printing, so not too many colours- 3-4 tops. Our primary logo colours are Green & blue.
There is both english and french text on the labels- see sample.
Our There are 2 main versions of the label and 1 sub version. (1 liter premixed, 3.78L and 20L concentrate. The concentrate is mixed at 10x the 1L premised is mixed at.
Our USPs are Very Effective, Very safe, Eviro-friendly, Versatile, low cost per use.
The product is sold in a natural(translucent) plastic jug, or bottle. The product itself is very pink in colour.
Target Market(s)
Outdoors- Powersports, RV, Mountainbike, Automotive, etc.
Industry/Entity Type
Automotive, RV, Powersports, Mountainbike, Farming, Household, Watercraft
Requirements
Must have
- English and french. It must communicate our USPs to the customer
Nice to have
- Bright bold colours, graphics and text.
Should not have
- Do no just do a re-hash of our existing label. I am looking for something different that really communicates to our customers.

```html
<!DOCTYPE html>
<html lang="en">
<head>
<meta charset="utf-8">
<title>Brisko Outdoor Cleaner – 1L Wrap Label</title>
<link href="https://fonts.googleapis.com/css2?family=Roboto+Condensed:wght@400;700&display=swap" rel="stylesheet">
<style>
  :root {
    --bg: #ececec;
    --paper: #ffffff;
    --navy: #1b2a8f;
    --blue: #2c63d0;
    --sky: #46a6ea;
    --ink-blue: #1f3a9c;
    --green: #34ad2a;
    --lime: #7fd62a;
    --ink-green: #52b82a;
    --body-ink: #333a4a;
    --rule: #d6dbe6;
  }
  * { margin: 0; padding: 0; box-sizing: border-box; }
  html, body { width: 1200px; height: 848px; overflow: hidden; background: var(--bg); }
  body { font-family: "Roboto Condensed", "Arial Narrow", sans-serif; font-weight: 700; }
  .canvas { position: relative; width: 1200px; height: 848px; }

  .label {
    position: absolute; left: 80px; top: 164px; width: 1040px; height: 520px;
    background: var(--paper); overflow: hidden;
    box-shadow: 0 10px 30px rgba(0,0,0,0.12);
  }
  .label-art { position: absolute; inset: 0; }

  /* side information panels */
  .info-panel {
    position: absolute; top: 140px; width: 230px; height: 250px;
    color: var(--body-ink); font-size: 13px; line-height: 1.4; font-weight: 400;
  }
  .info-panel.en { left: 30px; }
  .info-panel.fr { right: 30px; }
  .info-title { font-weight: 700; font-size: 15px; color: var(--ink-blue); margin-bottom: 6px; }
  .info-panel.fr .info-title { color: var(--ink-green); }
  .info-note { font-weight: 700; margin-top: 10px; }
  .panel-rule { position: absolute; top: 140px; width: 1px; height: 240px; background: var(--rule); }
  .panel-rule.left { left: 280px; }
  .panel-rule.right { left: 760px; }

  /* front panel */
  .front { position: absolute; left: 280px; top: 0; width: 480px; height: 520px; }
  .brand {
    position: absolute; left: 34px; top: 128px;
    display: flex; align-items: center; gap: 10px;
  }
  .brand-dot { width: 20px; height: 20px; border-radius: 50%; background: var(--lime); }
  .brand-name { font-size: 36px; line-height: 1; color: var(--ink-blue); letter-spacing: 1px; }
  .claims { position: absolute; left: 0; right: 0; top: 196px; text-align: center; }
  .claim { font-size: 19px; line-height: 1.25; }
  .claim.en { color: var(--ink-blue); }
  .claim.fr { color: var(--ink-green); }
  .claims .gap { height: 16px; }
  .claim.big { font-size: 20px; }
  .spec {
    position: absolute; right: 40px; top: 322px;
    display: flex; align-items: center; gap: 10px; color: var(--ink-blue);
  }
  .warning { font-size: 12px; line-height: 1.15; text-align: center; }
  .volume { font-size: 46px; line-height: 1; }

  .usp-strip {
    position: absolute; left: 0; right: 0; bottom: 26px;
    color: var(--paper); font-size: 14px; text-align: center; white-space: nowrap;
  }
</style>
</head>
<body>
<div class="canvas">
  <section class="label">
    <svg class="label-art" viewBox="0 0 1040 520" width="1040" height="520">
      <defs>
        <linearGradient id="topBand" x1="0" y1="0" x2="1" y2="1">
          <stop offset="0" stop-color="#46a6ea"/>
          <stop offset="0.5" stop-color="#2c63d0"/>
          <stop offset="1" stop-color="#1b2a8f"/>
        </linearGradient>
        <linearGradient id="bottomBand" x1="0" y1="0" x2="1" y2="0">
          <stop offset="0" stop-color="#34ad2a"/>
          <stop offset="1" stop-color="#7fd62a"/>
        </linearGradient>
      </defs>
      <g role="img" aria-label="Blue band with a field of dots">
        <path d="M0 0 H1040 V96 C880 128 760 110 600 80 C440 52 300 60 0 90 Z" fill="url(#topBand)"/>
      </g>
      <path d="M0 90 C300 60 440 52 600 80 C760 110 880 128 1040 96 V106 C880 140 760 120 600 90 C440 62 300 70 0 100 Z" fill="#46a6ea"/>
      <path d="M0 100 C300 70 440 62 600 90 C760 120 880 140 1040 106 V112 C880 148 760 128 600 96 C440 68 300 76 0 106 Z" fill="#1b2a8f"/>
      <g role="img" aria-label="Green band with a field of dots">
        <path d="M0 432 C220 396 420 404 600 436 C780 468 900 450 1040 420 V520 H0 Z" fill="url(#bottomBand)"/>
      </g>
      <path d="M0 424 C220 388 420 396 600 428 C780 460 900 442 1040 412 V420 C900 450 780 468 600 436 C420 404 220 396 0 432 Z" fill="#34ad2a"/>
    </svg>

    <div class="info-panel en">
      <p class="info-title">DIRECTIONS</p>
      <p>Spray directly on dirty surface. Let sit one to two minutes. Scrub stubborn spots with a soft brush. Rinse well with clean water. Do not let dry in direct sun.</p>
      <p class="info-note">Keep out of reach of children.</p>
    </div>
    <span class="panel-rule left"></span>

    <div class="front">
      <div class="brand">
        <span class="brand-dot"></span>
        <span class="brand-name">BRISKO</span>
      </div>

      <div class="claims">
        <p class="claim en">PRE-MIXED, READY TO USE</p>
        <p class="claim fr">PRÉ-MÉLANGÉ, PRÊT À L'EMPLOI</p>
        <div class="gap"></div>
        <p class="claim en big">THE EASY WAY TO CLEAN YOUR OUTDOOR STUFF!</p>
        <p class="claim fr big">UNE MANIÈRE DE NETTOYER VOS TRUCS EXTÉRIEURE!</p>
      </div>

      <div class="spec">
        <p class="warning">CAUTION<br>ATTENTION:<br>IRRITANT</p>
        <p class="volume">1L</p>
      </div>
    </div>

    <span class="panel-rule right"></span>
    <div class="info-panel fr">
      <p class="info-title">MODE D'EMPLOI</p>
      <p>Vaporiser directement sur la surface sale. Laisser agir une à deux minutes. Frotter les taches tenaces avec une brosse douce. Rincer à l'eau claire.</p>
      <p class="info-note">Garder hors de la portée des enfants.</p>
    </div>

    <p class="usp-strip">EASY TO USE • VERY EFFECTIVE &amp; VERSATILE • VERY AFFORDABLE! • ENVIRONMENTALLY FRIENDLY</p>
  </section>
</div>
</body>
</html>
```